Horse related business entrepreneur needs a business card

I need a business card design for my horse related business. The enterprise is Copper Fen LLC and I have 3 businesses (headquartered at 2 locations): 1. property management where we rent horse stalls and apartments at a thoroughbred training center outside Ocala; 2. a medium sized transportation service in central Florida that sells horse bedding and removes used horse bedding from horse farms; and horse racing

```html
<!DOCTYPE html>
<html lang="en">
<head>
<meta charset="utf-8">
<title>Copper Fen LLC – Business Card</title>
<link href="https://fonts.googleapis.com/css2?family=Montserrat:wght@400;500;700;800&family=Rubik:wght@400;500;700&display=swap" rel="stylesheet">
<style>
  :root {
    --backdrop: #5a5a5c;
    --card-light: #ffffff;
    --card-dark: #232323;
    --ink: #1f1f1f;
    --ink-soft: #d6d6d6;
    --accent: #e0302a;
  }
  * { margin: 0; padding: 0; box-sizing: border-box; }
  html, body { width: 1200px; height: 900px; overflow: hidden; }
  body {
    background: var(--backdrop);
    font-family: "Montserrat", sans-serif;
    position: relative;
  }
  .card {
    position: absolute;
    left: 250px;
    width: 700px;
    height: 400px;
    box-shadow: 0 10px 30px rgba(0,0,0,.35);
  }
  .card--front { top: 40px; background: var(--card-light); }
  .card--back { top: 460px; background: var(--card-dark); }

  /* front */
  .brand {
    position: absolute;
    left: 50px; top: 170px;
    width: 260px;
    display: flex; align-items: center; gap: 12px;
  }
  .brand__mark { width: 18px; height: 18px; background: var(--accent); flex: none; }
  .brand__name {
    font-family: "Montserrat", sans-serif;
    font-weight: 800;
    font-size: 30px;
    line-height: 1.05;
    color: var(--ink);
    letter-spacing: .5px;
  }
  .divider-vertical {
    position: absolute;
    left: 350px; top: 110px;
    width: 2px; height: 180px;
    background: var(--accent);
  }
  .contact {
    position: absolute;
    left: 390px; top: 120px;
    font-family: "Rubik", sans-serif;
    color: var(--ink);
  }
  .contact__name { font-size: 28px; font-weight: 700; color: var(--accent); }
  .contact__role { font-size: 20px; font-weight: 400; margin-top: 2px; margin-bottom: 16px; }
  .contact__row {
    display: flex; align-items: center; gap: 12px;
    font-size: 20px; line-height: 32px;
  }
  .contact__row svg { width: 20px; height: 20px; flex: none; }

  /* back */
  .back-brand {
    position: absolute;
    left: 0; right: 0; top: 110px;
    display: flex; justify-content: center; align-items: center; gap: 16px;
  }
  .back-brand .brand__mark { width: 24px; height: 24px; }
  .back-brand .brand__name { font-size: 48px; color: var(--ink-soft); }
  .addresses {
    position: absolute;
    left: 0; right: 0; top: 250px;
    display: flex; justify-content: center; align-items: center; gap: 30px;
    color: var(--ink-soft);
    font-size: 17px; line-height: 1.45; font-weight: 500;
  }
  .addresses__sep { width: 2px; height: 52px; background: var(--accent); }
</style>
</head>
<body>
  <section class="card card--front">
    <div class="brand">
      <span class="brand__mark"></span>
      <span class="brand__name">COPPER FEN LLC</span>
    </div>
    <div class="divider-vertical"></div>
    <div class="contact">
      <div class="contact__name">Dane Whitlock</div>
      <div class="contact__role">Owner</div>
      <div class="contact__row">
        <svg viewBox="0 0 20 20" fill="none" stroke="#e0302a" stroke-width="1.8"><rect x="5" y="1.5" width="10" height="17" rx="2"/><line x1="9" y1="15.5" x2="11" y2="15.5"/></svg>
        <span>(555) 018-2274</span>
      </div>
      <div class="contact__row">
        <svg viewBox="0 0 20 20" fill="#e0302a"><rect x="5" y="2" width="10" height="5"/><rect x="1.5" y="7" width="17" height="8" rx="1.5"/><rect x="5" y="12" width="10" height="6" fill="#fff" stroke="#e0302a" stroke-width="1.5"/></svg>
        <span>(555) 018-6630</span>
      </div>
      <div class="contact__row">
        <svg viewBox="0 0 20 20" fill="none" stroke="#e0302a" stroke-width="1.8"><rect x="2" y="4.5" width="16" height="11" rx="1"/><polyline points="2,5 10,11 18,5"/></svg>
        <span>dane@copperfen.com</span>
      </div>
    </div>
  </section>

  <section class="card card--back">
    <div class="back-brand">
      <span class="brand__mark"></span>
      <span class="brand__name">COPPER FEN LLC</span>
    </div>
    <div class="addresses">
      <div class="addresses__item">1720 SE 92 Lane<br>Marlow, FL 32690</div>
      <div class="addresses__sep"></div>
      <div class="addresses__item">5814 Alder Ridge Way<br>Westbury, VA 22910</div>
    </div>
  </section>
</body>
</html>
```